VORLEN Pathology

I have a website on vorlenpathology.pagebloom.com which I need further customized. This is a pathology/laboratory website. an example of my previous website is at brisendpath.com. We provide expertise in Dermatopathology & Anatomic Pathology to the Physicians & Patients since 2010.

Target Market(s)

Other medical professionals/doctors

Industry/Entity Type

Pathology, laboratory, medical doctor

Coding

Coded - Design and coding required

Number of Pages Required

4 page

Font styles to use
Serif
Sans Serif

Colors

Designer to choose colors to be used in the design.

Requirements
Must have
• Clean modern design, easy navigation

```html
<!DOCTYPE html>
<html lang="en">
<head>
<meta charset="utf-8">
<title>VORLEN Pathology</title>
<link rel="stylesheet" href="https://fonts.googleapis.com/css2?family=Michroma&family=Roboto:wght@400;500;700&display=swap">
<style>
:root{
  --purple:#5a22a8;
  --green:#8fd65a;
  --heading:#2b2b2b;
  --text:#6b6b6b;
  --nav:#2d2d2d;
  --footer-bg:#f4f4f4;
  --white:#ffffff;
}
*{margin:0;padding:0;box-sizing:border-box}
html,body{width:1200px;height:3185px;overflow:hidden;background:var(--white)}
body{position:relative;font-family:'Roboto',sans-serif;color:var(--text)}
.abs{position:absolute}
.display{font-family:'Michroma',sans-serif;color:var(--heading);letter-spacing:1px;text-transform:uppercase}
.btn{position:absolute;display:flex;align-items:center;justify-content:center;border-radius:26px;background:var(--purple);color:var(--white);font-weight:700;font-size:14.5px;text-transform:uppercase}
.brand-name{font-weight:700;color:var(--heading);font-size:26px;line-height:1;white-space:nowrap}
.social{display:flex;gap:9px}
.social span{width:34px;height:34px;border-radius:50%;background:var(--white);box-shadow:0 2px 6px rgba(0,0,0,.22)}
.social span:first-child{background:var(--purple)}
.top-line{left:0;top:0;width:1200px;height:5px;background:var(--green)}
.nav{left:404px;top:46px;display:flex;gap:24px;font-size:13.5px;font-weight:500;color:var(--nav);text-transform:uppercase}
.nav .active{color:var(--purple)}
.hero-copy{left:0;width:1200px;text-align:center;color:var(--white)}
.arrow{position:absolute;width:38px;height:38px;border-radius:50%;border:2px solid var(--white)}
.arrow svg{position:absolute;left:11px;top:11px}
.para{font-size:14px;line-height:25px;text-align:justify}
.card{position:absolute;top:1510px;width:313px;height:351px;background:var(--white);border-radius:3px;text-align:center;padding-top:35px}
.card h3{margin-top:24px;color:#2a53a8;font-size:18.5px;font-weight:700;text-transform:uppercase;letter-spacing:.5px}
.card p{margin:12px auto 0;width:275px;font-size:14px;line-height:25px}
.card .plus{width:38px;height:38px;border-radius:50%;background:var(--purple);margin:28px auto 0;display:flex;align-items:center;justify-content:center;color:#fff;font-weight:700;font-size:20px}
.foot-col h4{font-size:16.5px;font-weight:500;color:var(--heading);text-transform:uppercase;margin-bottom:16px}
.foot-col li{list-style:none;display:flex;align-items:center;gap:22px;font-size:15.5px;color:var(--text);height:29px}
.dot{width:13px;height:13px;border-radius:50%;background:var(--green);flex:none}
</style>
</head>
<body>

<div class="abs top-line"></div>
<div class="abs brand-name" style="left:111px;top:40px">VORLEN Pathology</div>
<nav class="abs nav">
  <span class="active">Home</span><span>Exceptional Pathology</span><span>About Us</span><span>Services</span><span>Contact Us</span>
</nav>
<div class="abs social" style="left:972px;top:36px"><span></span><span></span><span></span></div>

<svg class="abs" style="left:0;top:98px" width="1200" height="640" viewBox="0 0 1200 640">
  <defs>
    <linearGradient id="heroFill" x1="0" y1="0" x2="0" y2="1">
      <stop offset="0" stop-color="#7a9cc8"/>
      <stop offset="0.35" stop-color="#b9c9d9"/>
      <stop offset="0.5" stop-color="#56682f"/>
      <stop offset="1" stop-color="#7f9a3a"/>
    </linearGradient>
  </defs>
  <path role="img" aria-label="Mountain valley landscape with green meadows" d="M0 0H1200V495Q600 700 0 495Z" fill="url(#heroFill)"/>
  <path d="M60 520Q600 690 1160 520" fill="none" stroke="#ffffff" stroke-width="3"/>
</svg>
<div class="abs hero-copy display" style="top:300px;font-size:33px;color:#fff">Vorlen Pathology</div>
<div class="abs hero-copy" style="top:358px;font-size:16.5px;line-height:27px;font-weight:500">Our goal at VORLEN Pathology is to provide you &amp; your patients<br>with a high level of accessibility</div>
<div class="btn" style="left:525px;top:436px;width:150px;height:50px">Get Started</div>
<div class="arrow" style="left:38px;top:343px"><svg width="12" height="12" viewBox="0 0 12 12"><path d="M8 1 3 6l5 5" fill="none" stroke="#fff" stroke-width="2"/></svg></div>
<div class="arrow" style="left:1125px;top:343px"><svg width="12" height="12" viewBox="0 0 12 12"><path d="M4 1l5 5-5 5" fill="none" stroke="#fff" stroke-width="2"/></svg></div>

<svg class="abs" style="left:105px;top:808px" width="430" height="420" viewBox="0 0 430 420">
  <circle cx="219" cy="209" r="204" fill="var(--green)"/>
  <circle cx="227" cy="209" r="204" fill="#ffffff"/>
  <circle cx="227" cy="209" r="198" fill="#d9d9d9"/>
  <circle role="img" aria-label="Portrait of Dr. Harlow" cx="227" cy="209" r="196" fill="#3d4a55"/>
</svg>
<h2 class="abs display" style="left:600px;top:845px;font-size:33px">About Us</h2>
<div class="abs" style="left:600px;top:912px;width:489px">
  <p class="para">Dr. Harlow is board certified in Dermatopathology and Anatomic Pathology. In addition, Dr. Harlow is fellowship trained in Surgical Pathology.</p>
  <p class="para" style="margin-top:15px">Dr. Harlow grew up in southern California and received her Bachelor of Science degree in Microbiology from the Pacific Coast University, Harbor College of Science and Engineering. She earned her medical degree and was elected to the Sigma Delta Medical Honor Society at Eastbrook University. Dr. Harlow then completed</p>
</div>
<div class="btn" style="left:600px;top:1135px;width:141px;height:50px">Learn More</div>

<svg class="abs" style="left:0;top:1316px" width="1200" height="690" viewBox="0 0 1200 690">
  <defs>
    <linearGradient id="svcFill" x1="0" y1="0" x2="1" y2="1">
      <stop offset="0" stop-color="#4274c6"/><stop offset="0.5" stop-color="#3a68bd"/><stop offset="1" stop-color="#3461b4"/>
    </linearGradient>
  </defs>
  <path role="img" aria-label="Blue tissue microscopy texture" d="M0 105Q600 -100 1200 105V590Q600 790 0 590Z" fill="url(#svcFill)"/>
</svg>
<h2 class="abs display" style="left:0;width:1200px;text-align:center;top:1424px;font-size:33px;color:#fff">Our Services</h2>
<div class="card" style="left:111px">
  <svg width="60" height="60" viewBox="0 0 60 60" fill="none" stroke="var(--green)" stroke-width="2.2"><path d="M10 55h36M20 55v-8h16v8M22 47c-8-4-8-16 2-19M26 8l12 7-10 18-12-7z"/><circle cx="42" cy="32" r="6"/><circle cx="48" cy="14" r="4"/></svg>
  <h3>Dermatopathology</h3>
  <p>Sed ut perspiciatis unde omnis iste nat us error sit voluptatem accusantium do lore mque laudantium, totam rem ape riam, eaque ipsa quae.</p>
  <div class="plus">+</div>
</div>
<div class="card" style="left:444px">
  <svg width="68" height="60" viewBox="0 0 68 60" fill="none" stroke="var(--green)" stroke-width="3"><path d="M34 56 8 30C-2 18 8 2 20 4c6 1 10 5 14 10 4-5 8-9 14-10 12-2 22 14 12 26z"/><path d="M8 32h14l5-9 6 16 5-11 4 4h16"/></svg>
  <h3>Anatomic Pathology</h3>
  <p>Sed ut perspiciatis unde omnis iste nat us error sit voluptatem accusantium do lore mque laudantium, totam rem ape riam, eaque ipsa quae.</p>
  <div class="plus">+</div>
</div>
<div class="card" style="left:776px">
  <svg width="60" height="60" viewBox="0 0 60 60" fill="none" stroke="var(--green)" stroke-width="2.2"><circle cx="30" cy="16" r="11"/><path d="M8 58V44c0-8 8-12 22-12s22 4 22 12v14zM24 33l6 10 6-10M18 40v8M42 40v10"/></svg>
  <h3>Physicians &amp; Patients</h3>
  <p>Sed ut perspiciatis unde omnis iste nat us error sit voluptatem accusantium do lore mque laudantium, totam rem ape riam, eaque ipsa quae.</p>
  <div class="plus">+</div>
</div>
<div class="arrow" style="left:38px;top:1667px"><svg width="12" height="12" viewBox="0 0 12 12"><path d="M8 1 3 6l5 5" fill="none" stroke="#fff" stroke-width="2"/></svg></div>
<div class="arrow" style="left:1125px;top:1667px"><svg width="12" height="12" viewBox="0 0 12 12"><path d="M4 1l5 5-5 5" fill="none" stroke="#fff" stroke-width="2"/></svg></div>

<h2 class="abs display" style="left:111px;top:2112px;font-size:33px;line-height:40px">Exceptional<br>Pathology</h2>
<div class="abs" style="left:111px;top:2217px;width:441px">
  <p class="para">Providing expertise in Dermatopathology &amp; Anatomic Pathology to the Physicians &amp; Patients of Northern Colorado.</p>
  <p class="para" style="margin-top:14px">At Brisend Pathology, we strive to provide you with exceptional pathology services. We believe that strong consultative relationships lead to the best possible care for every patient.</p>
</div>
<div class="btn" style="left:111px;top:2390px;width:141px;height:50px">Learn More</div>
<div class="abs" style="left:645px;top:2084px;width:444px;height:367px;background:var(--green);border-radius:10px"></div>
<div class="abs" style="left:632px;top:2094px;width:446px;height:370px;background:#fff;border-radius:10px;box-shadow:0 3px 10px rgba(0,0,0,.2)"></div>
<div class="abs" role="img" aria-label="Microscope objective lens in blue light" style="left:639px;top:2101px;width:431px;height:355px;border-radius:6px;background:linear-gradient(135deg,#1d2f8c,#4a6be0 45%,#aebff0 60%,#2a3ea8)"></div>

<div class="abs" role="img" aria-label="Purple-tinted desk with paperwork" style="left:0;top:2550px;width:1200px;height:315px;background:linear-gradient(120deg,#5a24a6,#6a35b8 60%,#5b2aa8)"></div>
<h2 class="abs display" style="left:0;width:1200px;text-align:center;top:2604px;font-size:28px;line-height:38px;color:#fff">Have a question about<br>your bill?</h2>
<p class="abs" style="left:0;width:1200px;text-align:center;top:2699px;font-size:16.5px;font-weight:500;color:#fff">Need a specimen pick up? Have questions about your bill? We look forward to hearing from you!</p>
<div class="btn" style="left:530px;top:2752px;width:141px;height:50px;background:#fff;color:var(--heading)">Contact Us</div>

<div class="abs" style="left:0;top:2865px;width:1200px;height:320px;background:var(--footer-bg)"></div>
<div class="abs brand-name" style="left:111px;top:2950px;font-size:28px">VORLEN Pathology</div>
<div class="abs social" style="left:185px;top:3034px"><span></span><span></span><span></span></div>
<div class="abs foot-col" style="left:448px;top:2920px">
  <h4>Quick Links</h4>
  <ul><li><i class="dot"></i>Home</li><li><i class="dot"></i>Exceptional Pathology</li><li><i class="dot"></i>About Us</li><li><i class="dot"></i>Services</li><li><i class="dot"></i>Contact Us</li></ul>
</div>
<div class="abs foot-col" style="left:696px;top:2920px">
  <h4>About Links</h4>
  <ul><li><i class="dot"></i>Site Map</li><li><i class="dot"></i>Privacy Policy</li><li><i class="dot"></i>Terms Of Use</li><li><i class="dot"></i>Legal Support</li></ul>
</div>
<div class="abs foot-col" style="left:885px;top:2920px">
  <h4>Contact</h4>
  <ul>
    <li><svg width="13" height="13" viewBox="0 0 13 13"><path d="M3 1l2 3-1.5 1.5a7 7 0 0 0 4 4L9 8l3 2-1 2C6 12 1 7 1 2z" fill="var(--green)"/></svg>(970) 555-0148</li>
    <li><svg width="13" height="13" viewBox="0 0 13 13"><rect x="1" y="5" width="11" height="7" fill="var(--green)"/><rect x="3" y="1" width="7" height="4" fill="var(--green)"/></svg>(970) 555-0172</li>
    <li><svg width="13" height="13" viewBox="0 0 13 13"><rect x="0" y="2" width="13" height="9" fill="var(--green)"/><path d="M0 2l6.5 5L13 2" fill="none" stroke="#fff"/></svg>iwm@brisendpath.com</li>
    <li><svg width="13" height="13" viewBox="0 0 13 13"><rect x="0" y="2" width="13" height="9" fill="var(--green)"/><path d="M0 2l6.5 5L13 2" fill="none" stroke="#fff"/></svg>info@brisendpath.com</li>
  </ul>
</div>
<div class="abs" style="left:111px;top:3137px;width:978px;height:1px;background:#dcdcdc"></div>
<p class="abs" style="left:453px;top:3152px;font-size:13px;color:var(--text)">© 2022 <b style="color:var(--heading);font-weight:500">VORLEN PATHOLOGY</b> &nbsp;/ &nbsp; All Rights Reserved</p>

</body>
</html>
```